Curl Radiant through and through. Hair stylist that specializes in extensions.

I am Marisol I am a hair stylist and I would like a website designed for my hair business.

I currently book clients via my profile on trimnook.example/marisolbrantley

I need a professional website ( curlradiantthroughandthrough.example ) to display photos and prices for services offered.

I would like to have a home page with a brief bio, Image with logo and testimonials at the bottom, and a header with tab that include: menu of services, gallery,and FAQs.

On the "Services" page, I'm not interested in photos on this page. Just the name of the service, brief description, and pricing. I would also like to have, on this page, "Appointment Request" with fields that include: Name, service requested, desired time frame (morning, afternoon, evening), and contact number and email

On the "Gallery" page, I would like pictures only, but arranged and/or presented in a creative way...

Target Market(s)

Women ages 25-55 who interested in hair extension services.

Industry/Entity Type

Hair And Beauty

Coding

Number of Pages Required

5+ page

Font styles to use
Sans Serif

Requirements
Must have
• Must include tabs that include, Menu of services offered, a quick fund link to pay deposits with ease, location, contact information, photo gallery, and policy/faqs.
Nice to have
• If possible i would like to stream music with the ability to be silenced. I would like a neutral color palette tans and beige.
Should not have
• stock images

```html
<!DOCTYPE html>
<html lang="en">
<head>
<meta charset="utf-8">
<title>Curl Radiant through and through</title>
<link rel="stylesheet" href="https://fonts.googleapis.com/css2?family=Raleway:wght@400;500;600&family=Bodoni+Moda:wght@400;500&family=Arimo:wght@400;700&display=swap">
<style>
:root{
  --ink:#222222;
  --grey:#5a5a5a;
  --muted:#8a8a8a;
  --line:#e2e2e2;
  --coral:#f46b6b;
  --sun:#f6c66a;
  --teal:#5fc3c7;
  --gold:#e2b857;
  --dark:#333333;
  --darker:#1e1e1e;
  --white:#ffffff;
}
*{box-sizing:border-box;margin:0;padding:0}
html,body{width:1200px;height:3243px;overflow:hidden;background:var(--white)}
body{font-family:"Arimo",Arial,sans-serif;color:var(--ink)}
.canvas{position:relative;width:1200px;height:3243px;overflow:hidden}
.photo{position:absolute}

/* hero */
.hero{position:absolute;left:0;top:0;width:1200px;height:655px;background:var(--white)}
.hero-photo{left:380px;top:160px;width:820px;height:495px;z-index:1;background:radial-gradient(ellipse at 45% 55%,#a9735a 0%,#6b4433 32%,#2a1c18 62%,#f4f1ee 100%)}
.brand{position:absolute;left:0;width:1200px;top:30px;text-align:center;font-family:"Raleway",sans-serif;z-index:2}
.brand-name{font-size:46px;font-weight:600;color:var(--ink);letter-spacing:2px;line-height:1.1}
.brand-tag{font-size:16px;font-weight:500;color:var(--ink);letter-spacing:5px;margin-top:6px;text-transform:uppercase}
.hero-title{position:absolute;left:22px;top:205px;font-family:"Raleway",sans-serif;color:var(--ink);z-index:2}
.hero-title .kicker{font-size:24px;font-weight:400;letter-spacing:1px}
.hero-title .big{font-size:100px;font-weight:400;line-height:.92;letter-spacing:-1px}
.hero-title .big.grey{color:var(--grey);padding-left:60px;font-weight:500}
.hero-title .sub{font-size:22px;font-weight:600;letter-spacing:3px;padding-left:118px;margin-top:2px}

/* nav */
.main-nav{position:absolute;left:0;top:655px;width:1200px;height:65px;border-top:1px solid var(--line);background:var(--white)}
.main-nav a{position:absolute;top:20px;font-family:"Arimo",sans-serif;font-size:18px;color:var(--muted);text-decoration:none;letter-spacing:.5px}
.main-nav a.current{color:var(--ink)}

/* services */
.service{position:absolute;width:400px;height:270px;color:var(--white);text-align:center;font-family:"Raleway",sans-serif}
.service h2{font-size:40px;font-weight:400;line-height:1;margin-top:22px}
.service h3{font-size:20px;font-weight:500;letter-spacing:1px}
.price-list{list-style:none;width:228px;margin:16px auto 0;text-align:left;font-family:"Arimo",sans-serif;font-size:14px}
.price-list li{display:flex;justify-content:space-between;padding:4px 0;border-bottom:1px solid rgba(255,255,255,.55)}
.price-list li:last-child{border-bottom:none}
.btn-request{display:inline-block;margin-top:18px;width:146px;height:48px;line-height:46px;font-family:"Arimo",sans-serif;font-size:19px;border:2px solid var(--white);color:var(--white);background:transparent}
.btn-request.solid{background:var(--white);border-color:var(--white)}
.service.basic{left:0;top:720px;background:var(--coral)}
.service.straight{left:800px;top:720px;background:var(--sun)}
.service.straight .btn-request{color:var(--sun)}
.service.color{left:400px;top:990px;background:var(--teal)}
.service.color .btn-request{color:var(--teal)}
.ph-blonde{left:400px;top:720px;width:400px;height:270px;background:radial-gradient(ellipse at 50% 40%,#f0dcb0 0%,#c9a36d 45%,#6f5a45 100%)}
.ph-curls{left:0;top:990px;width:400px;height:270px;background:radial-gradient(ellipse at 55% 50%,#7a4432 0%,#3c2019 55%,#1d1210 100%)}
.ph-bob{left:800px;top:990px;width:400px;height:270px;background:radial-gradient(ellipse at 55% 50%,#8a5b48 0%,#4b2c24 40%,#d8d2cc 100%)}

/* testimonial */
.testimonial{position:absolute;left:0;top:1260px;width:1200px;height:524px;background:radial-gradient(ellipse at 75% 55%,#5a5a5a 0%,#3a3a3a 45%,#262626 100%);color:var(--white);text-align:center}
.testimonial h2{position:absolute;left:0;width:1200px;top:62px;font-family:"Bodoni Moda",serif;font-weight:400;font-size:36px;line-height:44px}
.testimonial h2 span{color:var(--gold)}
.quote-mark{position:absolute;font-family:"Bodoni Moda",serif;font-size:70px;line-height:1}
.quote-text{position:absolute;left:303px;top:196px;width:594px;font-size:15px;line-height:26px}
.avatar{position:absolute;left:558px;top:284px;width:84px;height:84px;border-radius:50%;border:3px solid var(--white);background:radial-gradient(circle at 50% 45%,#e8d6c8 0%,#a88a78 70%)}
.client{position:absolute;left:0;width:1200px;top:375px;font-size:22px;font-family:"Raleway",sans-serif}
.dots{position:absolute;left:555px;top:456px;display:flex;gap:20px}
.dots i{width:11px;height:11px;border-radius:50%;background:var(--white);display:block}
.dots i.off{background:transparent;border:2px solid var(--white)}

/* gallery */
.gallery-title{position:absolute;left:0;width:1200px;top:1850px;text-align:center;font-family:"Bodoni Moda",serif;font-size:40px;font-weight:400;color:var(--ink)}
.gallery-tabs a{position:absolute;top:1926px;font-size:15px;color:var(--muted);text-decoration:none}
.gallery-tabs a.current{color:var(--ink);border-bottom:2px dashed var(--ink);padding-bottom:6px}
.tile{position:absolute;width:261px;height:313px}
.t-brunette{background:radial-gradient(ellipse at 45% 40%,#7a4c35 0%,#4a2a1d 45%,#e9e5e0 100%)}
.t-meadow{background:radial-gradient(ellipse at 55% 45%,#e4d2b4 0%,#a99c74 50%,#5b6447 100%)}
.t-bridal{background:radial-gradient(ellipse at 50% 45%,#b67c56 0%,#e4d8cf 60%,#f4f0ec 100%)}
.t-curly{background:radial-gradient(ellipse at 50% 45%,#8a5340 0%,#4d2b22 45%,#cfc7bf 100%)}
.btn-view{position:absolute;left:508px;top:2681px;width:186px;height:47px;background:#8f8f8f;color:var(--white);text-align:center;line-height:47px;font-size:18px}

/* cta */
.cta{position:absolute;left:0;top:2782px;width:1200px;height:180px;background:var(--teal);color:var(--white)}
.cta .pledge{position:absolute;left:80px;top:70px;font-family:"Bodoni Moda",serif;font-size:17px;letter-spacing:1px}
.cta .make{position:absolute;left:80px;top:94px;font-family:"Bodoni Moda",serif;font-size:36px;letter-spacing:1px}
.cta .phone{position:absolute;left:820px;top:64px;font-family:"Bodoni Moda",serif;font-size:46px}

/* footer */
.site-footer{position:absolute;left:0;top:2962px;width:1200px;height:227px;background:var(--dark);color:#d6d6d6;font-size:15px}
.site-footer h4{position:absolute;top:31px;font-family:"Bodoni Moda",serif;font-weight:500;font-size:16px;color:var(--white)}
.foot-line{position:absolute;display:flex;align-items:flex-start;gap:14px;line-height:26px}
.foot-line svg{flex:none;margin-top:3px}
.foot-link{position:absolute;color:#d6d6d6;text-decoration:none}
.hours{position:absolute;left:832px;top:74px;width:248px;text-align:center}
.hours div{height:38px;line-height:34px;border-bottom:1px solid #555}
.hours div:last-child{border-bottom:none}
.bottom-bar{position:absolute;left:0;top:3189px;width:1200px;height:54px;background:var(--darker);color:var(--white)}
.bottom-bar p{position:absolute;left:80px;top:18px;font-family:"Bodoni Moda",serif;font-size:13px}
.bottom-bar p u{text-decoration:underline}
.social{position:absolute;left:1010px;top:20px;display:flex;gap:22px}
.social i{display:block;width:13px;height:13px;border-radius:50%;background:var(--white)}
</style>
</head>
<body>
<div class="canvas">

  <header class="hero">
    <div class="photo hero-photo" role="img" aria-label="Portrait of two women with long glossy dark hair"></div>
    <div class="brand">
      <div class="brand-name">CURL RADIANT</div>
      <div class="brand-tag">Through and through</div>
    </div>
    <div class="hero-title">
      <div class="kicker">PROFESSIONAL</div>
      <div class="big">HAIR</div>
      <div class="big grey">CARE</div>
      <div class="sub">SOLUTIONS</div>
    </div>
  </header>

  <nav class="main-nav">
    <a class="current" style="left:270px">HOME</a>
    <a style="left:372px">ABOUT</a>
    <a style="left:484px">SERVICE</a>
    <a style="left:608px">GALLERY</a>
    <a style="left:741px">FAQS</a>
    <a style="left:840px">CONTACT</a>
  </nav>

  <section class="service basic">
    <h2>BASIC</h2>
    <h3>SERVICES</h3>
    <ul class="price-list">
      <li><span>Cleanse / Style</span><span>$45*</span></li>
      <li><span>Custom Cut Design</span><span>$35</span></li>
      <li><span>Wand Curls</span><span>$25</span></li>
    </ul>
    <span class="btn-request">REQUEST</span>
  </section>
  <div class="photo ph-blonde" role="img" aria-label="Woman with windswept blonde hair"></div>
  <section class="service straight">
    <h2>STRAGHTENING</h2>
    <h3>SERVICES</h3>
    <ul class="price-list">
      <li><span>Chemical Straighteners</span><span>$65</span></li>
      <li><span>Silk Press</span><span>$65</span></li>
    </ul>
    <span class="btn-request solid" style="margin-top:46px">REQUEST</span>
  </section>
  <div class="photo ph-curls" role="img" aria-label="Woman with voluminous dark curls"></div>
  <section class="service color">
    <h2>COLOR</h2>
    <h3>SERVICES</h3>
    <ul class="price-list">
      <li><span>High &amp; Low Lights</span><span>$130*</span></li>
      <li><span>Permanent Color</span><span>$125*</span></li>
      <li><span>Semi-permanent color</span><span>$25*</span></li>
    </ul>
    <span class="btn-request solid">REQUEST</span>
  </section>
  <div class="photo ph-bob" role="img" aria-label="Smiling woman with a glossy brown bob"></div>

  <section class="testimonial" role="img" aria-label="Background photo of a stylist's hands in dark hair">
    <h2>Giving You Legendary Haircut with<br><span>Traditional Services</span></h2>
    <span class="quote-mark" style="left:240px;top:166px">“</span>
    <p class="quote-text">"I have been looking for a stylist since I moved to Dallas for 7 years. I noticed a young ladys hair and she gave me Marisol information. I LOVE MY HAIR. She does an amazing job. Always leave satisfied!!!"</p>
    <span class="quote-mark" style="left:922px;top:236px">”</span>
    <div class="avatar" role="img" aria-label="Client portrait"></div>
    <div class="client">RENATA V.</div>
    <div class="dots"><i></i><i></i><i class="off"></i></div>
  </section>

  <h2 class="gallery-title">Check Out Our Gallery</h2>
  <nav class="gallery-tabs">
    <a class="current" style="left:372px">Show All</a>
    <a style="left:497px">Hair Cut</a>
    <a style="left:620px">Hair Color</a>
    <a style="left:755px">Hair Style</a>
  </nav>
  <div class="tile t-brunette" style="left:78px;top:2002px" role="img" aria-label="Woman with sleek asymmetric brown bob"></div>
  <div class="tile t-meadow" style="left:339px;top:2002px" role="img" aria-label="Blonde woman with braided crown in a meadow"></div>
  <div class="tile t-bridal" style="left:600px;top:2002px" role="img" aria-label="Bridal updo with flowers"></div>
  <div class="tile t-curly" style="left:861px;top:2002px" role="img" aria-label="Woman with long auburn curls"></div>
  <div class="tile t-curly" style="left:78px;top:2315px" role="img" aria-label="Woman with long auburn curls"></div>
  <div class="tile t-bridal" style="left:339px;top:2315px" role="img" aria-label="Bridal updo with flowers"></div>
  <div class="tile t-meadow" style="left:600px;top:2315px" role="img" aria-label="Blonde woman with braided crown in a meadow"></div>
  <div class="tile t-brunette" style="left:861px;top:2315px" role="img" aria-label="Woman with sleek asymmetric brown bob"></div>
  <div class="btn-view">VIEW ALL</div>

  <section class="cta">
    <div class="pledge">WE PLEDGE TO CARE FOR YOU</div>
    <div class="make">MAKE AN APPOINTMENT NOW</div>
    <div class="phone">817-555-0164</div>
  </section>

  <footer class="site-footer">
    <h4 style="left:80px">Contact us</h4>
    <div class="foot-line" style="left:82px;top:68px;width:340px">
      <svg width="22" height="28" viewBox="0 0 22 28"><path d="M11 26C11 26 2 15 2 10a9 9 0 0 1 18 0c0 5-9 16-9 16z" fill="none" stroke="#d6d6d6" stroke-width="1.6"/><circle cx="11" cy="10" r="3.2" fill="none" stroke="#d6d6d6" stroke-width="1.6"/></svg>
      <span>48 Fernhollow Lane, 2 Marlow Green<br>CR9 4QT</span>
    </div>
    <div class="foot-line" style="left:82px;top:133px">
      <svg width="22" height="22" viewBox="0 0 22 22"><path d="M5 2l4 5-2 3c1 3 3 5 6 6l3-2 5 4-3 3C9 21 1 13 2 5z" fill="none" stroke="#d6d6d6" stroke-width="1.6" stroke-linejoin="round"/></svg>
      <span>0208 555 0147, 0770 555 0192</span>
    </div>
    <div class="foot-line" style="left:82px;top:174px">
      <svg width="22" height="18" viewBox="0 0 22 18"><rect x="1" y="2" width="20" height="14" fill="none" stroke="#d6d6d6" stroke-width="1.6"/><path d="M1 2l10 8 10-8" fill="none" stroke="#d6d6d6" stroke-width="1.6"/></svg>
      <span>bookings@curlradiant.example</span>
    </div>

    <h4 style="left:486px">Navigation Links</h4>
    <a class="foot-link" style="left:486px;top:74px">Home</a>
    <a class="foot-link" style="left:486px;top:104px">About</a>
    <a class="foot-link" style="left:486px;top:137px">Services</a>
    <a class="foot-link" style="left:486px;top:167px">Gallery</a>
    <a class="foot-link" style="left:633px;top:74px">Faq's</a>
    <a class="foot-link" style="left:633px;top:104px">Contact</a>
    <a class="foot-link" style="left:633px;top:137px">Blog</a>
    <a class="foot-link" style="left:633px;top:167px">Terms</a>

    <h4 style="left:895px">Business Hours</h4>
    <div class="hours">
      <div>Tuesday - 9AM to 6PM</div>
      <div>Wednesday - 9PM to 6PM</div>
      <div>Thursday - 9PM to 6PM</div>
    </div>
  </footer>

  <div class="bottom-bar">
    <p>© <u>Curl Radiant through and through</u> 2016. All Rights Reserved</p>
    <div class="social"><i></i><i></i><i></i><i></i></div>
  </div>

</div>
</body>
</html>
```